Tradeshwo display 8x10 high resolution backdrop

I created a backdrop I wanted to use via Chat GPT but the image isn't high quality enough for print so I want someone to recreate it as close as possible to my creation. See attached, TY!

```html
<!DOCTYPE html>
<html lang="en">
<head>
<meta charset="utf-8">
<title>Northline – Tradeshow Backdrop</title>
<link rel="stylesheet" href="https://fonts.googleapis.com/css2?family=Rubik:wght@700;800;900&family=Montserrat:ital,wght@0,400;0,500;0,700;0,800;1,800&family=Barlow+Condensed:wght@500;600&display=swap">
<style>
:root{
  --stage:#b3b3b3;
  --ink:#1f1f1f;
  --blue:#0b3fb0;
  --blue-deep:#0a2f8a;
  --navy:#15264a;
  --navy-dark:#0e1b36;
  --line:#2f6fe0;
  --white:#ffffff;
  --black:#000000;
  --slogan:#1f52d6;
}
*{box-sizing:border-box;margin:0;padding:0}
html,body{width:1200px;height:971px;overflow:hidden;background:var(--stage)}
.backdrop{position:absolute;left:40px;top:58px;width:1120px;height:854px;background:var(--white);overflow:hidden;font-family:"Montserrat",sans-serif;color:var(--ink)}
.art{position:absolute;inset:0}
.abs{position:absolute}

.brand{left:16px;top:20px;width:290px;height:140px;display:flex;flex-direction:column;justify-content:center;align-items:flex-start;padding-left:18px}
.brand-name{font-family:"Rubik",sans-serif;font-weight:900;font-size:38px;color:var(--blue-deep);letter-spacing:.5px;line-height:1;display:flex;align-items:center;gap:8px;white-space:nowrap}
.brand-name .dot{width:18px;height:18px;border-radius:50%;background:var(--blue-deep)}
.brand-sub{font-family:"Montserrat",sans-serif;font-weight:700;font-size:13px;color:var(--ink);margin-top:8px}

.values{top:48px;left:326px;display:flex}
.value{width:102px;text-align:center;font-size:12.5px;line-height:15px;color:#222;font-weight:500;border-right:1px solid #9aa3b3;height:92px;display:flex;flex-direction:column;align-items:center;justify-content:space-between;padding-top:2px}
.value:last-child{border-right:none}
.value svg{width:44px;height:44px}

.headline{left:0;width:860px;top:178px;text-align:center;font-family:"Rubik",sans-serif;font-weight:900;line-height:1}
.headline .l1{font-size:64px;color:var(--ink);letter-spacing:1px}
.headline .l2{font-size:66px;color:var(--blue-deep);letter-spacing:1px}

.tagline{left:55px;width:755px;top:312px;display:flex;align-items:center;gap:22px;font-size:21px;color:var(--ink);white-space:nowrap}
.tagline::before,.tagline::after{content:"";flex:1;height:1px;background:#555}

.pill{left:23px;top:354px;width:816px;height:49px;border-radius:25px;background:var(--blue);color:var(--white);font-weight:700;font-size:20px;display:flex;align-items:center;justify-content:center;letter-spacing:.2px}

.products{left:15px;top:414px;width:842px;display:flex}
.product{width:140px;text-align:center;border-right:1px solid #b7bcc6;padding:0 4px;height:310px}
.product:last-child{border-right:none}
.product-img{width:122px;height:138px;margin:0 auto;border-radius:24px;background:radial-gradient(circle at 50% 55%,#3b63c7 0%,#6f86bf 45%,#f2f4f8 75%)}
.product-img.grey{background:radial-gradient(circle at 50% 55%,#8a8d92 0%,#b3b6bb 45%,#f3f4f6 75%)}
.product-img.dark{background:radial-gradient(circle at 50% 55%,#2b3340 0%,#5a6170 40%,#f2f3f5 72%)}
.product-img.icon{background:radial-gradient(circle at 50% 50%,#1d4fd0 0%,#6e8ee0 35%,#ffffff 70%)}
.product h3{font-family:"Rubik",sans-serif;font-weight:800;color:var(--blue);font-size:17px;line-height:15px;margin-top:18px;height:32px;display:flex;align-items:flex-start;justify-content:center}
.product p{font-size:13.5px;line-height:16px;color:#222;max-width:108px;margin:0 auto}

.pillars{left:858px;top:278px;width:262px}
.pillar{position:absolute;left:0;width:262px;height:108px;display:flex;align-items:center}
.pillar svg.frame{position:absolute;inset:0}
.pillar .icon{position:relative;margin-left:30px;width:58px;height:58px}
.pillar .txt{position:relative;margin-left:10px;font-family:"Barlow Condensed",sans-serif;font-weight:600;font-size:20px;line-height:19px;color:var(--white);text-transform:uppercase}

.footer{left:0;top:754px;width:1120px;height:100px;display:flex;align-items:center;color:var(--white)}
.service{display:flex;align-items:center;gap:10px;margin-left:27px;width:428px}
.service b{display:block;font-size:16px;font-weight:800}
.service span{font-size:11px;letter-spacing:.2px}
.service i{color:var(--slogan);font-style:normal;margin:0 6px}
.web{width:268px;height:40px;border-left:1px solid #ccc;border-right:1px solid #ccc;display:flex;align-items:center;justify-content:center;font-weight:700;font-size:15.5px}
.slogan{flex:1;text-align:center;font-style:italic;font-weight:800;font-size:21px;line-height:25px;color:var(--slogan)}
</style>
</head>
<body>
<main class="backdrop">
  <svg class="art" viewBox="0 0 1120 854">
    <defs>
      <linearGradient id="sky" x1="0" y1="0" x2="0" y2="1">
        <stop offset="0" stop-color="#5c86c0"/>
        <stop offset=".35" stop-color="#c9c6b4"/>
        <stop offset=".55" stop-color="#3f5a4a"/>
        <stop offset="1" stop-color="#1c3c6e"/>
      </linearGradient>
      <linearGradient id="panel" x1="0" y1="0" x2="1" y2="0">
        <stop offset="0" stop-color="#1a2c52"/>
        <stop offset="1" stop-color="#0f1d3b"/>
      </linearGradient>
    </defs>
    <path d="M700,0 L735,0 C745,120 810,215 900,280 L1120,280 L1120,740 L858,740 L858,290 C780,230 715,130 700,0Z" fill="var(--navy-dark)"/>
    <path d="M712,0 L726,0 C738,125 800,220 885,282 L870,284 C790,225 722,130 712,0Z" fill="var(--line)"/>
    <g role="img" aria-label="Photo of a water treatment plant with circular clarifier tanks at sunset under a cloudy sky">
      <path d="M740,0 L1120,0 L1120,278 L905,278 C820,215 752,125 740,0Z" fill="url(#sky)"/>
    </g>
    <path d="M0,700 C320,735 700,745 1120,695 L1120,735 C700,790 320,775 0,745Z" fill="var(--blue-deep)"/>
    <path d="M0,725 C320,760 700,770 1120,720 L1120,735 C700,785 320,770 0,740Z" fill="var(--line)"/>
    <path d="M0,738 C320,770 700,780 1120,735 L1120,854 L0,854Z" fill="var(--black)"/>
  </svg>

  <div class="abs brand">
    <div class="brand-name"><span class="dot"></span>NORTHLINE</div>
    <div class="brand-sub">Flow Systems &amp; Equipment</div>
  </div>

  <div class="abs values">
    <div class="value">
      <svg viewBox="0 0 44 44" fill="none" stroke="var(--blue)" stroke-width="2"><circle cx="22" cy="17" r="13"/><circle cx="22" cy="17" r="8"/><path d="M18 17l3 3 5-6"/><path d="M14 27l-4 12 6-3 3 5 3-10M30 27l4 12-6-3-3 5-3-10"/></svg>
      <span>QUALITY<br>BRANDS</span>
    </div>
    <div class="value">
      <svg viewBox="0 0 44 44" fill="none" stroke="var(--blue)" stroke-width="2"><circle cx="22" cy="22" r="7"/><path d="M19 4h6l1 5 4 2 4-3 4 4-3 4 2 4 5 1v6l-5 1-2 4 3 4-4 4-4-3-4 2-1 5h-6l-1-5-4-2-4 3-4-4 3-4-2-4-5-1v-6l5-1 2-4-3-4 4-4 4 3 4-2z"/></svg>
      <span>ENGINEERED<br>SOLUTIONS</span>
    </div>
    <div class="value">
      <svg viewBox="0 0 44 44" fill="none" stroke="var(--blue)" stroke-width="2"><path d="M8 24v-4a14 14 0 0 1 28 0v4"/><rect x="6" y="22" width="6" height="11" rx="3"/><rect x="32" y="22" width="6" height="11" rx="3"/><path d="M35 33c0 5-5 7-11 7"/><circle cx="22" cy="40" r="2"/></svg>
      <span>EXPERT<br>SUPPORT</span>
    </div>
    <div class="value">
      <svg viewBox="0 0 44 44" fill="none" stroke="var(--blue)" stroke-width="2" stroke-linejoin="round"><path d="M2 14l8-4 12 6 12-6 8 4v12l-6 3"/><path d="M2 14v12l6 3 10 8c2 1 4 0 4-2"/><path d="M22 16l-7 6c-1 2 1 4 3 3l6-4 10 9c2 1 0 4-2 3"/><path d="M14 31l4 4M18 29l4 4M24 33l3 2"/></svg>
      <span>TURNKEY<br>DELIVERY</span>
    </div>
  </div>

  <h1 class="abs headline"><div class="l1">SOLUTIONS THAT</div><div class="l2">KEEP WATER MOVING</div></h1>

  <div class="abs tagline">EXPERTISE. RELIABILITY. RESULTS</div>

  <div class="abs pill">COMPLETE SOLUTIONS FOR THE WATER &amp; WASTEWATER INDUSTRY</div>

  <section class="abs products">
    <article class="product"><div class="product-img" role="img" aria-label="Blue horizontal split-case pump"></div><h3>PUMPS</h3><p>Industry leading pumps built for performance, efficiency &amp; reliability.</p></article>
    <article class="product"><div class="product-img" role="img" aria-label="Blue industrial electric motor"></div><h3>MOTORS</h3><p>High efficiency motors engineered for durability and long life.</p></article>
    <article class="product"><div class="product-img grey" role="img" aria-label="Grey positive displacement blower"></div><h3>BLOWERS</h3><p>Aerix PD positive displacement blowers for reliable, energy efficient performance.</p></article>
    <article class="product"><div class="product-img dark" role="img" aria-label="Variable frequency drive cabinet with keypad"></div><h3>VFD &amp;<br>CONTROLS</h3><p>Precision control and energy savings through advanced VFD solutions.</p></article>
    <article class="product"><div class="product-img" role="img" aria-label="Blue control valve with actuator"></div><h3>AUTOMATION<br>&amp; VALVES</h3><p>Smart automation and reliable valves for optimized system performance.</p></article>
    <article class="product"><div class="product-img icon" role="img" aria-label="Illustration of a hand holding a gear with a water drop"></div><h3>TURNKEY<br>SOLUTIONS</h3><p>Complete systems designed, integrated and supported by Northline.</p></article>
  </section>

  <section class="abs pillars">
    <div class="pillar" style="top:0">
      <svg class="frame" viewBox="0 0 262 108"><path d="M262,0H22L0,54L22,108H262Z" fill="url(#panel)" stroke="var(--line)" stroke-width="1.5"/></svg>
      <svg class="icon" viewBox="0 0 58 58" fill="none" stroke="#fff" stroke-width="2.5"><circle cx="29" cy="29" r="26"/><path d="M29 13c-6 9-10 14-10 19a10 10 0 0 0 20 0c0-5-4-10-10-19z"/><path d="M24 33a5 5 0 0 0 5 5"/></svg>
      <div class="txt">WATER &amp; WASTE-<br>WATER EXPERTISE</div>
    </div>
    <div class="pillar" style="top:116px">
      <svg class="frame" viewBox="0 0 262 108"><path d="M262,0H22L0,54L22,108H262Z" fill="url(#panel)" stroke="var(--line)" stroke-width="1.5"/></svg>
      <svg class="icon" viewBox="0 0 58 58" fill="none" stroke="#fff" stroke-width="2.5"><path d="M29 3l22 8v16c0 14-10 24-22 28C17 51 7 41 7 27V11z"/><path d="M29 10l16 6v11c0 10-7 18-16 21-9-3-16-11-16-21V16z"/><path d="M21 29l6 6 10-11"/></svg>
      <div class="txt">TRUSTED<br>PRODUCTS</div>
    </div>
    <div class="pillar" style="top:230px">
      <svg class="frame" viewBox="0 0 262 108"><path d="M262,0H22L0,54L22,108H262Z" fill="url(#panel)" stroke="var(--line)" stroke-width="1.5"/></svg>
      <svg class="icon" viewBox="0 0 58 58" fill="none" stroke="#fff" stroke-width="2.5"><path d="M10 30v-4a19 19 0 0 1 38 0v4"/><rect x="5" y="27" width="9" height="15" rx="4"/><rect x="44" y="27" width="9" height="15" rx="4"/><path d="M48 42c0 7-8 10-17 10"/><circle cx="29" cy="52" r="3"/></svg>
      <div class="txt">LOCAL SUPPORT<br>YOU CAN COUNT<br>ON</div>
    </div>
    <div class="pillar" style="top:346px">
      <svg class="frame" viewBox="0 0 262 108"><path d="M262,0H22L0,54L22,108H262Z" fill="url(#panel)" stroke="var(--line)" stroke-width="1.5"/></svg>
      <svg class="icon" viewBox="0 0 58 58" fill="none" stroke="#fff" stroke-width="2.5"><circle cx="29" cy="29" r="26"/><path d="M16 44V34M24 44V30M32 44V26M40 44V20" stroke-width="5"/><path d="M15 28l10-8 6 4 11-10M36 14h6v6"/></svg>
      <div class="txt">BUILT FOR<br>PERFORMANCE.<br>FOCUSED ON<br>YOUR SUCCESS.</div>
    </div>
  </section>

  <footer class="abs footer">
    <div class="service">
      <svg width="22" height="30" viewBox="0 0 22 30"><path d="M11 0C5 0 0 5 0 11c0 8 11 19 11 19s11-11 11-19C22 5 17 0 11 0z" fill="#fff"/><circle cx="11" cy="11" r="4.5" fill="#000"/></svg>
      <div><b>SERVICING:</b><span>VIRGINIA<i>•</i>NORTH CAROLINA<i>•</i>MARYLAND<i>•</i>DELAWARE</span></div>
    </div>
    <div class="web">www.northline-flow.com</div>
    <div class="slogan">YOUR PARTNER FOR A<br>BETTER FLOW FORWARD</div>
  </footer>
</main>
</body>
</html>
```